Heritage Hollow Business Cards

Require a business card design. <br/><br/>Needs to include logo (either round or long version) plus these details:<br/>Maya Torvel<br/>Heritage Hollow<br/>maya@quonbrook.com.au<br/>02 6481 7390<br/>PO Box Glenwarra NSW 2913<br/>www.heritagehollow.com.au<br/><br/>I need in an editable format so that I can create for multiple staff members. <br/><br/>

Target Market(s)

We are an online store selling renovation products to home owners are builders. Looking for a classic classy design.

Industry/Entity Type

Home And Garden

Contact Information for Business Card

Maya Torvel
Heritage Hollow
maya@quonbrook.com.au
02 6481 7390
PO Box Glenwarra NSW 2913
www.heritagehollow.com.au

Colors

Designer to choose colors to be used in the design.

Requirements
Must have
• Must include Logo.

```html
<!DOCTYPE html>
<html lang="en">
<head>
<meta charset="utf-8">
<title>Heritage Hollow Business Cards</title>
<link href="https://fonts.googleapis.com/css2?family=Arvo:wght@400;700&display=swap" rel="stylesheet">
<style>
  :root {
    --backdrop: #9a9a99;
    --card-front: #7a7a79;
    --card-back: #ffffff;
    --ink: #6b6b6b;
    --ink-light: #ffffff;
    --rule: #8a8a8a;
  }
  html, body {
    margin: 0;
    padding: 0;
    width: 1200px;
    height: 965px;
    overflow: hidden;
    background: var(--backdrop);
    font-family: "Arvo", serif;
  }
  .canvas {
    position: relative;
    width: 1200px;
    height: 965px;
  }
  .card {
    position: absolute;
    left: 278px;
    width: 646px;
    height: 368px;
    border-radius: 22px;
    overflow: hidden;
  }
  .card--front { top: 98px; background: var(--card-front); }
  .card--back { top: 504px; background: var(--card-back); }

  .brand-mark {
    position: absolute;
    border-radius: 50%;
    display: flex;
    align-items: center;
    justify-content: center;
    text-align: center;
    box-sizing: border-box;
  }
  .card--front .brand-mark {
    left: 200px; top: 65px; width: 236px; height: 236px;
    border: 1px solid var(--ink-light);
  }
  .card--back .brand-mark {
    left: 348px; top: 70px; width: 288px; height: 288px;
    border: 1px solid var(--rule);
  }
  .brand-name {
    font-weight: 400;
    line-height: 1.05;
    padding-top: 70px;
  }
  .card--front .brand-name { color: var(--ink-light); font-size: 30px; }
  .card--back .brand-name { color: var(--ink); font-size: 36px; padding-top: 86px; }

  .details {
    position: absolute;
    left: 26px;
    top: 148px;
    color: var(--ink);
    font-weight: 700;
  }
  .details__name {
    margin: 0;
    font-size: 19px;
    letter-spacing: 1.5px;
    text-transform: uppercase;
  }
  .details__company {
    margin: 4px 0 0;
    font-size: 14px;
  }
  .details__address {
    margin: 26px 0 0;
    font-size: 14px;
    line-height: 24px;
    font-style: normal;
  }
  .contact-list {
    list-style: none;
    margin: 12px 0 0;
    padding: 0;
    font-size: 14px;
  }
  .contact-list li {
    display: flex;
    align-items: center;
    height: 23.5px;
  }
  .contact-list svg {
    width: 14px;
    height: 14px;
    margin-right: 12px;
    fill: var(--ink);
  }
</style>
</head>
<body>
<main class="canvas">
  <section class="card card--front" aria-label="Card front">
    <div class="brand-mark">
      <span class="brand-name">Heritage<br>Hollow</span>
    </div>
  </section>

  <section class="card card--back" aria-label="Card back">
    <div class="details">
      <h1 class="details__name">Maya Torvel</h1>
      <p class="details__company">Heritage Hollow</p>
      <address class="details__address">PO Box Glenwarra<br>NSW 2913</address>
      <ul class="contact-list">
        <li>
          <svg viewBox="0 0 16 16" aria-hidden="true"><path d="M3.5 1.5l2.5 0 1 3.5-1.8 1.2c.8 1.8 2.2 3.2 4 4l1.2-1.8 3.5 1v2.5c0 .8-.7 1.5-1.5 1.5C6.8 13.4 2.6 9.2 2 3c0-.8.7-1.5 1.5-1.5z"/></svg>
          02 6481 7390
        </li>
        <li>
          <svg viewBox="0 0 16 16" aria-hidden="true"><path d="M1 3h14v10H1zM2.2 4.2v.4L8 8.8l5.8-4.2v-.4zM2.2 6v5.8h11.6V6L8 10.2z"/></svg>
          maya@quonbrook.com.au
        </li>
        <li>
          <svg viewBox="0 0 16 16" aria-hidden="true"><path d="M8 1a7 7 0 1 0 0 14A7 7 0 0 0 8 1zm0 1.4c.9.9 1.5 2.6 1.7 4.6H6.3C6.5 5 7.1 3.3 8 2.4zM2.5 8.6h2.4c.1 1.9.6 3.5 1.3 4.6A5.6 5.6 0 0 1 2.5 8.6zm0-1.6a5.6 5.6 0 0 1 3.7-4.2C5.5 3.8 5 5.2 4.9 7zm5.5 6.6c-.9-.9-1.5-2.6-1.7-5h3.4c-.2 2.4-.8 4.1-1.7 5zm1.8-.4c.7-1.1 1.2-2.7 1.3-4.6h2.4a5.6 5.6 0 0 1-3.7 4.6zM11.1 7c-.1-1.8-.6-3.2-1.3-4.2A5.6 5.6 0 0 1 13.5 7z"/></svg>
          www.www.heritagehollow.com.au
        </li>
      </ul>
    </div>
    <div class="brand-mark">
      <span class="brand-name">Heritage<br>Hollow</span>
    </div>
  </section>
</main>
</body>
</html>
```